Brightwell Power Solutions

We'd like a web design that's beautiful and professional. We replace existing inefficient systems (mostly lighting at the moment but expanding) with highly efficient systems.

```html
<!DOCTYPE html>
<html lang="en">
<head>
<meta charset="utf-8">
<title>Brightwell Power Solutions</title>
<link href="https://fonts.googleapis.com/css2?family=PT+Sans:wght@400;700&family=PT+Sans+Narrow:wght@400;700&family=Open+Sans:wght@400;700&display=swap" rel="stylesheet">
<style>
:root{
  --green:#00a651;
  --green-dark:#008c44;
  --header:#1b1b1b;
  --nav-active:#141414;
  --page:#eff1ef;
  --panel:#f3f4f3;
  --card:#ffffff;
  --heading:#555a5a;
  --text:#6b6f6f;
  --footer:#353535;
  --footer-bottom:#262626;
  --footer-text:#a9a9a9;
}
*{margin:0;padding:0;box-sizing:border-box}
html,body{width:1024px;height:1200px;overflow:hidden}
body{position:relative;background:var(--page);font-family:'PT Sans',sans-serif;color:var(--text)}
.abs{position:absolute}

.site-header{left:0;top:0;width:1024px;height:83px;background:var(--header)}
.brand{left:136px;top:0;width:116px;height:96px;background:#fff;border-radius:0 0 6px 6px;box-shadow:0 2px 4px rgba(0,0,0,.3);display:flex;flex-direction:column;align-items:center;justify-content:center;gap:6px;text-align:center;z-index:3}
.brand-mark{width:14px;height:14px;background:var(--green)}
.brand-name{font-family:'PT Sans Narrow',sans-serif;font-weight:700;font-size:14px;line-height:1.05;color:var(--green)}
.main-nav{left:532px;top:0;height:83px;display:flex}
.nav-item{height:83px;text-align:center;padding-top:30px;font-family:'PT Sans Narrow',sans-serif}
.nav-item.active{background:var(--nav-active)}
.nav-item b{display:block;font-size:13px;color:#fff;font-weight:700}
.nav-item span{display:block;font-size:7px;color:#8a8a8a;font-family:'Open Sans',sans-serif;margin-top:2px}
.nav-item.active b{color:var(--green)}

.hero-band{left:0;top:83px;width:1024px;height:398px;background:var(--green);border-bottom:2px solid #fff}
.slider{left:128px;top:109px;width:768px;height:301px;background:linear-gradient(100deg,#3a4a62 0%,#8a90a0 30%,#d9dcdf 55%,#eceeef 100%)}
.slide-caption{left:629px;top:217px;width:233px;height:165px;background:rgba(245,246,246,.88);padding:14px 20px}
.slide-caption h2{font-family:'PT Sans Narrow',sans-serif;font-size:20px;font-weight:400;color:#222}
.slide-caption p{font-size:9.5px;line-height:14.5px;color:#666;margin-top:10px}
.btn-dark{display:inline-block;margin-top:18px;width:88px;height:31px;line-height:31px;text-align:center;background:linear-gradient(#6a6a6a,#474747);color:#fff;font-size:10px;font-weight:700;border-radius:2px}
.arrow{width:38px;height:38px;border-radius:50%;border:3px solid rgba(255,255,255,.4)}
.arrow svg{display:block}

.content-panel{left:108px;top:439px;width:803px;height:578px;background:var(--panel);border-radius:3px;box-shadow:0 10px 22px rgba(0,0,0,.1)}
.card{background:var(--card);border-radius:3px;box-shadow:0 1px 3px rgba(0,0,0,.12)}
.welcome{left:128px;top:464px;width:504px;height:206px}
.welcome-photo{left:0;top:0;width:172px;height:206px;background:linear-gradient(160deg,#e9c84a,#c68c3a 45%,#8a5a30);border-radius:3px 0 0 3px}
h3.title{font-family:'PT Sans Narrow',sans-serif;font-weight:700;font-size:18px;color:var(--heading)}
h3.title em{font-style:normal;color:var(--green)}
.welcome-body{left:183px;top:30px;width:300px}
.welcome-body p{font-size:9.5px;line-height:16px;margin-top:14px}
.btn-light{display:inline-block;height:28px;line-height:26px;padding:0 9px;background:linear-gradient(#f3f3f3,#e1e1e1);border:1px solid #cfcfcf;border-radius:2px;font-size:8.5px;color:#7a7a7a;box-shadow:0 1px 2px rgba(0,0,0,.1)}
.welcome-body .btn-light{margin-top:14px}
.why{left:648px;top:464px;width:240px;height:206px;padding:30px 17px}
.why ul{list-style:none;margin-top:14px}
.why li{display:flex;align-items:center;gap:10px;font-size:9.5px;height:27px}
.tick{width:14px;height:14px;flex:none}

.section-title{left:0;top:702px;width:1024px;text-align:center;font-family:'PT Sans Narrow',sans-serif;font-weight:700;font-size:20px;letter-spacing:1px;color:#6a6e6e}
.service{width:240px}
.service-photo{width:240px;height:100px;border:3px solid #fff;box-shadow:0 1px 3px rgba(0,0,0,.25)}
.service h4{font-size:12px;font-weight:700;color:#666;margin:24px 0 0 3px}
.service p{font-size:9.5px;line-height:16px;margin:14px 0 0 3px}
.service .btn-light{margin:14px 0 0 4px}

.site-footer{left:0;top:1017px;width:1024px;height:147px;background:var(--footer);border-top:2px solid #2a2a2a}
.footer-brand{left:137px;top:23px;width:122px;height:101px;border:2px solid #222;background:#3d3d3d;display:flex;flex-direction:column;align-items:center;justify-content:center;gap:6px;text-align:center}
.footer-brand .brand-name{color:var(--green-dark)}
.footer-brand .brand-mark{background:var(--green-dark)}
.fcol h5{font-size:11.5px;font-weight:700;color:#fff;margin-bottom:12px}
.fcol ul{list-style:none}
.fcol li{font-family:'Open Sans',sans-serif;font-size:8.5px;color:var(--footer-text);height:19.2px;display:flex;align-items:center;gap:6px}
.fcol li.current{color:#2f8fd8}
.caret{width:3px;height:5px;flex:none}
.contact li{height:24px;gap:10px}
.contact li.cont{padding-left:21px;margin-top:-5px}
.ico{width:11px;height:11px;flex:none}
.social{display:flex;gap:8px}
.social span{width:28px;height:28px;border-radius:3px;box-shadow:0 1px 2px rgba(0,0,0,.4)}
.bottom-bar{left:0;top:1164px;width:1024px;height:36px;background:var(--footer-bottom);font-family:'Open Sans',sans-serif;font-size:8.5px;color:var(--footer-text)}
.bottom-bar .copy{left:126px;top:12px}
.bottom-bar .links{right:137px;top:12px}
</style>
</head>
<body>

<header class="abs site-header">
  <div class="abs brand"><div class="brand-mark"></div><div class="brand-name">BRIGHTWELL POWER<br>SOLUTIONS</div></div>
  <nav class="abs main-nav">
    <div class="nav-item active" style="width:72px"><b>HOME</b><span>Start here</span></div>
    <div class="nav-item" style="width:84px"><b>ABOUT</b><span>Know us</span></div>
    <div class="nav-item" style="width:88px"><b>SERVICES</b><span>Our Work</span></div>
    <div class="nav-item" style="width:116px"><b>CONTACT US</b><span>Get in touch</span></div>
  </nav>
</header>

<section class="abs hero-band"></section>
<div class="abs slider" role="img" aria-label="Photo of an electrician in a hard hat working at an electrical distribution board"></div>
<div class="abs slide-caption">
  <h2>Featured Headline</h2>
  <p>Lorem ipsum dolor sit amet, consectetur adipisicing elit, sed do eiusmod tempor incididunt ut labore et dolore magna.</p>
  <span class="btn-dark">Read More</span>
</div>
<div class="abs arrow" style="left:109px;top:235px;background:var(--green)">
  <svg width="32" height="32" viewBox="0 0 32 32"><path d="M17.5 12.5 14 16l3.5 3.5" fill="none" stroke="#fff" stroke-width="1.6"/></svg>
</div>
<div class="abs arrow" style="left:879px;top:235px;background:#333">
  <svg width="32" height="32" viewBox="0 0 32 32"><path d="M14.5 12.5 18 16l-3.5 3.5" fill="none" stroke="#fff" stroke-width="1.6"/></svg>
</div>

<main class="abs content-panel"></main>

<article class="abs card welcome">
  <div class="abs welcome-photo" role="img" aria-label="Photo of a smiling electrician in a yellow hard hat carrying a coil of cable"></div>
  <div class="abs welcome-body">
    <h3 class="title">Welcome to <em>Brightwell Power Solutions</em></h3>
    <p>Lorem ipsum dolor sit amet, consectetur adipisicing elit, sed do eiusmod tempor incididunt ut labore et dolore magna aliqua. Ut enim ad minim veniam, quis nostrud exercitation ullamco laboris nisi ut aliquip ex ea commodo consequat.</p>
    <span class="btn-light">Learn More</span>
  </div>
</article>

<aside class="abs card why">
  <h3 class="title">Why Choose Us?</h3>
  <ul>
    <li><svg class="tick" viewBox="0 0 14 14"><circle cx="7" cy="7" r="7" fill="#5cb85c"/><path d="M6 4.5 8.5 7 6 9.5" fill="none" stroke="#fff" stroke-width="1.6"/></svg>Cras rutrum leo at odio volutpat id blan</li>
    <li><svg class="tick" viewBox="0 0 14 14"><circle cx="7" cy="7" r="7" fill="#5cb85c"/><path d="M6 4.5 8.5 7 6 9.5" fill="none" stroke="#fff" stroke-width="1.6"/></svg>Donec fermentum porttitor nunc, sit amet</li>
    <li><svg class="tick" viewBox="0 0 14 14"><circle cx="7" cy="7" r="7" fill="#5cb85c"/><path d="M6 4.5 8.5 7 6 9.5" fill="none" stroke="#fff" stroke-width="1.6"/></svg>Maecenas quis nisi in uctus adipiscing sed</li>
    <li><svg class="tick" viewBox="0 0 14 14"><circle cx="7" cy="7" r="7" fill="#5cb85c"/><path d="M6 4.5 8.5 7 6 9.5" fill="none" stroke="#fff" stroke-width="1.6"/></svg>Aenean faucibus sapien a odio varius</li>
  </ul>
</aside>

<h2 class="abs section-title">OUR SERVICES</h2>

<div class="abs service" style="left:136px;top:740px">
  <div class="service-photo" role="img" aria-label="Photo of an electrician wiring a control panel" style="background:linear-gradient(90deg,#2c3a55,#5a6478 50%,#c9c2a0)"></div>
  <h4>Electrical Installation</h4>
  <p>Lid est laborum dolo rumes fugats untras. Etharums ser quidem rerum facilis dolores nemis omnis fugats vitaes nemo minima rerums unsers</p>
  <span class="btn-light">Learn More</span>
</div>
<div class="abs service" style="left:394px;top:740px">
  <div class="service-photo" role="img" aria-label="Photo of an engineer in an orange hard hat beside a utility pole" style="background:linear-gradient(90deg,#c9502f,#7fb0dc 45%,#9fcbef)"></div>
  <h4>Energy Management</h4>
  <p>Lid est laborum dolo rumes fugats untras. Etharums ser quidem rerum facilis dolores nemis omnis fugats vitaes nemo minima rerums unsers</p>
  <span class="btn-light">Learn More</span>
</div>
<div class="abs service" style="left:648px;top:740px">
  <div class="service-photo" role="img" aria-label="Photo of a power transmission tower in a green field under blue sky" style="background:linear-gradient(180deg,#2f7fd0,#8cc2ee 70%,#6fae3c 88%)"></div>
  <h4>Renewable Energy</h4>
  <p>Lid est laborum dolo rumes fugats untras. Etharums ser quidem rerum facilis dolores nemis omnis fugats vitaes nemo minima rerums unsers</p>
  <span class="btn-light">Learn More</span>
</div>

<footer class="abs site-footer">
  <div class="abs footer-brand"><div class="brand-mark"></div><div class="brand-name">BRIGHTWELL POWER<br>SOLUTIONS</div></div>
  <div class="abs fcol" style="left:321px;top:24px">
    <h5>Navigation</h5>
    <ul>
      <li><svg class="caret" viewBox="0 0 3 5"><path d="M0 0l3 2.5L0 5z" fill="#888"/></svg>Home</li>
      <li><svg class="caret" viewBox="0 0 3 5"><path d="M0 0l3 2.5L0 5z" fill="#888"/></svg>About</li>
      <li><svg class="caret" viewBox="0 0 3 5"><path d="M0 0l3 2.5L0 5z" fill="#888"/></svg>Services</li>
      <li><svg class="caret" viewBox="0 0 3 5"><path d="M0 0l3 2.5L0 5z" fill="#888"/></svg>Contact</li>
    </ul>
  </div>
  <div class="abs fcol" style="left:449px;top:24px">
    <h5>Services</h5>
    <ul>
      <li class="current"><svg class="caret" viewBox="0 0 3 5"><path d="M0 0l3 2.5L0 5z" fill="#888"/></svg>Menu1</li>
      <li><svg class="caret" viewBox="0 0 3 5"><path d="M0 0l3 2.5L0 5z" fill="#888"/></svg>Menu1</li>
      <li><svg class="caret" viewBox="0 0 3 5"><path d="M0 0l3 2.5L0 5z" fill="#888"/></svg>Menu1</li>
      <li><svg class="caret" viewBox="0 0 3 5"><path d="M0 0l3 2.5L0 5z" fill="#888"/></svg>Menu1</li>
    </ul>
  </div>
  <div class="abs fcol contact" style="left:577px;top:24px">
    <h5>Contact Us</h5>
    <ul>
      <li><svg class="ico" viewBox="0 0 12 12"><path d="M2.5 1h2l1 3-1.5 1a7 7 0 0 0 3 3l1-1.5 3 1v2c0 .6-.4 1-1 1A10 10 0 0 1 1.5 2c0-.6.4-1 1-1z" fill="#8a8a8a"/></svg>+1800-123-4567</li>
      <li><svg class="ico" viewBox="0 0 12 12"><rect x="1" y="3" width="10" height="7" fill="#8a8a8a"/><path d="M1 3l5 4 5-4" fill="none" stroke="#353535" stroke-width="1"/></svg>info@yourwebsite.com</li>
      <li><svg class="ico" viewBox="0 0 12 12"><path d="M6 1a3.5 3.5 0 0 0-3.5 3.5C2.5 7.5 6 11 6 11s3.5-3.5 3.5-6.5A3.5 3.5 0 0 0 6 1z" fill="#8a8a8a"/><circle cx="6" cy="4.5" r="1.3" fill="#353535"/></svg>Your Address, Your Country</li>
      <li class="cont">Your Zip Code</li>
    </ul>
  </div>
  <div class="abs fcol" style="left:750px;top:24px">
    <h5>Social</h5>
    <div class="social">
      <span style="background:#3b5998"></span>
      <span style="background:#2fa8e0"></span>
      <span style="background:#0e6aa5"></span>
      <span style="background:#d73d32"></span>
    </div>
  </div>
</footer>

<div class="abs bottom-bar">
  <span class="abs copy">Copyright 2014 © CompanyName - All Rights Reserved</span>
  <span class="abs links">Site Map &nbsp; • &nbsp; Privacy Policy</span>
</div>

</body>
</html>
```